Brightstep Dance Business Card

I'm looking for a two-sided business card design to promote my country dance busness. Cowboy hats, boots, and wood grain floor textures, are all appropriate to use.
On one side I want it to say:
Brightstep Dance
with
Mark
Take The Challenge - Experience The Growth
210-555-0143
On the other side I want:
A place for a Head Shot
The Quote: Experience Is The Best Teacher
A two column bullet list with the following:
First column: Two Step, Waltz, Triple Two, Polka
Second column: Cha-Cha, West Coast, East Cost, NightClub
My Name: Mark Delway
My Phone Number: 210-555-0143

```html
<!DOCTYPE html>
<html lang="en">
<head>
<meta charset="utf-8">
<title>Brightstep Dance – Business Card</title>
<link rel="stylesheet" href="https://fonts.googleapis.com/css2?family=Cinzel:wght@500;600&family=Michroma&family=Poppins:wght@400;500;600;700&display=swap">
<style>
  :root {
    --backdrop: #1c1c1c;
    --navy: #034c78;
    --navy-deep: #023a5e;
    --green: #5a931e;
    --white: #ffffff;
    --photo-light: #d9d9dc;
    --photo-dark: #9a9a9e;
    --ink: #3a3a3a;
  }
  * { box-sizing: border-box; margin: 0; padding: 0; }
  html, body {
    width: 1093px;
    height: 1200px;
    overflow: hidden;
    background: var(--backdrop);
  }
  .canvas { position: relative; width: 1093px; height: 1200px; }

  .card {
    position: absolute;
    left: 264px;
    width: 580px;
    height: 357px;
    overflow: hidden;
    background: var(--navy);
    color: var(--white);
  }
  .card--front { top: 226px; }
  .card--back  { top: 620px; }

  .band {
    position: absolute;
    left: 0; right: 0; bottom: 0;
    background: var(--green);
  }
  .card--front .band { top: 242px; }
  .card--back  .band { top: 248px; }

  /* front */
  .dancer-faint {
    position: absolute;
    left: 0; top: 30px;
    width: 380px; height: 212px;
    background: radial-gradient(ellipse at 45% 55%, var(--navy-deep) 0%, rgba(2,58,94,0.5) 45%, rgba(2,58,94,0) 72%);
  }
  .dancer-pair {
    position: absolute;
    left: 380px; top: 52px;
    width: 130px; height: 190px;
    background: linear-gradient(180deg, rgba(90,147,30,0.35), rgba(90,147,30,0.85));
    border-radius: 60px 60px 0 0;
  }
  .brand {
    position: absolute;
    left: 63px; top: 22px;
    font: 700 37px/1 "Poppins", sans-serif;
    letter-spacing: -0.3px;
    white-space: nowrap;
  }
  .with {
    position: absolute;
    left: 174px; top: 84px;
    font: 600 20px/1 "Poppins", sans-serif;
    letter-spacing: 3px;
  }
  .first-name {
    position: absolute;
    left: 82px; top: 120px;
    font: 500 86px/1 "Cinzel", serif;
    letter-spacing: 1px;
    white-space: nowrap;
  }
  .tagline {
    position: absolute;
    left: 0; right: 0; top: 260px;
    text-align: center;
    font: 600 20px/1 "Poppins", sans-serif;
    letter-spacing: 0.6px;
    text-transform: uppercase;
    white-space: nowrap;
  }
  .phone {
    position: absolute;
    font-family: "Michroma", sans-serif;
    font-weight: 400;
    line-height: 1;
    white-space: nowrap;
    -webkit-text-stroke: 1px var(--white);
  }
  .card--front .phone {
    left: 0; right: 0; top: 300px;
    text-align: center;
    font-size: 29px;
    letter-spacing: 3px;
  }

  /* back */
  .headshot {
    position: absolute;
    left: 30px; top: 38px;
    width: 193px; height: 230px;
    border: 3px solid var(--white);
    border-radius: 2px;
    background: radial-gradient(ellipse at 50% 40%, var(--photo-light), var(--photo-dark));
  }
  .headshot__label {
    position: absolute;
    left: 0; right: 0; bottom: 14px;
    text-align: center;
    font: 400 19px/1 "Poppins", sans-serif;
    color: var(--ink);
  }
  .name-tag {
    position: absolute;
    left: 30px; top: 280px;
    width: 193px; height: 40px;
    background: var(--navy);
    text-align: center;
    font: 600 25px/40px "Poppins", sans-serif;
    white-space: nowrap;
  }
  .name-tag::before {
    content: "";
    position: absolute;
    left: 8px; top: -8px;
    border: 5px solid transparent;
    border-bottom: 8px solid var(--navy);
    border-top: 0;
  }
  .quote {
    position: absolute;
    left: 250px; top: 36px;
    width: 300px;
    text-align: center;
    font: 600 28px/35px "Cinzel", serif;
    letter-spacing: 0.5px;
  }
  .styles {
    position: absolute;
    top: 128px;
    list-style: none;
    font: 500 21px/26px "Poppins", sans-serif;
    white-space: nowrap;
  }
  .styles--one { left: 259px; }
  .styles--two { left: 412px; }
  .styles li { position: relative; padding-left: 18px; }
  .styles li::before {
    content: "";
    position: absolute;
    left: 0; top: 10px;
    width: 7px; height: 7px;
    border-radius: 50%;
    background: var(--white);
  }
  .card--back .phone {
    left: 250px; top: 287px;
    font-size: 25px;
    letter-spacing: 2px;
  }
</style>
</head>
<body>
<main class="canvas">

  <section class="card card--front">
    <div class="dancer-faint" role="img" aria-label="Faint silhouette of a dancer in a deeper navy tone"></div>
    <div class="dancer-pair" role="img" aria-label="Green silhouette of two dancers performing a lift"></div>
    <h1 class="brand">Brightstep Dance</h1>
    <p class="with">WITH</p>
    <p class="first-name">MARK</p>
    <div class="band"></div>
    <p class="tagline">Take The Challenge - Experience The Growth</p>
    <p class="phone">210-555-0143</p>
  </section>

  <section class="card card--back">
    <div class="band"></div>
    <div class="headshot" role="img" aria-label="Head shot photo of Mark Delway">
      <span class="headshot__label">PHOTO HERE</span>
    </div>
    <p class="name-tag">Mark Delway</p>
    <p class="quote">Experience Is The<br>Best Teacher</p>
    <ul class="styles styles--one">
      <li>Two Step</li>
      <li>Waltz</li>
      <li>Triple Two</li>
      <li>Polka</li>
    </ul>
    <ul class="styles styles--two">
      <li>Cha-Cha</li>
      <li>West Coast</li>
      <li>East Cost</li>
      <li>NightClub</li>
    </ul>
    <p class="phone">210-555-0143</p>
  </section>

</main>
</body>
</html>
```